I Need a Banner for Web Advertising

impression banner for zentora AD
size 728x90, 320x50 , 160x600 , 300x600 , 100x50
Banner background bright blue
would like the AD to say -
We pay cash for houses in any condition
Probate,foreclosure, Pass due property taxes ect
470-555-0193
Updates
We would like to change the words to -
We pay cash for houses in any condition!
Probate, Foreclosure, Pass Due Property Taxes, and more!
470-555-0193
Target Market(s)
consumers that need to sale
Industry/Entity Type
Real Estate

```html
<!DOCTYPE html>
<html lang="en">
<head>
<meta charset="utf-8">
<title>Zentora Web Banner Set</title>
<link rel="stylesheet" href="https://fonts.googleapis.com/css2?family=Poppins:wght@300;400;600;700;800&family=Noto+Serif:wght@400&display=swap">
<style>
  :root{
    --navy:#0a0a6b;
    --blue:#0791d0;
    --orange:#f9a24b;
    --green:#9acb3b;
    --yellow:#ffcc00;
    --pink:#f0125d;
    --ink:#111111;
    --white:#ffffff;
    --dusk-a:#c9d6ea;
    --dusk-b:#4f5f86;
    --siding:#a8a08a;
  }
  *{box-sizing:border-box;margin:0;padding:0}
  html,body{width:1200px;height:1200px;overflow:hidden;background:var(--navy)}
  body{position:relative;font-family:"Poppins",sans-serif;color:var(--white)}
  .size-label{position:absolute;font-weight:600;font-size:37px;line-height:1;white-space:nowrap;color:var(--white)}
  .banner{position:absolute;overflow:hidden;background:var(--blue)}
  .banner svg.shapes{position:absolute;inset:0;width:100%;height:100%}
  .photo{position:absolute}
  .photo-dusk{background:linear-gradient(180deg,var(--dusk-a) 0%,#8b9ac0 40%,var(--dusk-b) 75%,#6a6a62 100%)}
  .photo-day{background:linear-gradient(180deg,#dfe6ee 0%,var(--siding) 45%,#8c8472 80%,#6b7a52 100%)}
  .brand{position:absolute;font-weight:800;color:var(--ink);line-height:1;white-space:nowrap;letter-spacing:.5px}
  .read-more{position:absolute;background:var(--pink);color:var(--white);font-weight:600;border-radius:3px;text-align:center;white-space:nowrap}
  .contact-label{position:absolute;font-weight:600;line-height:1;white-space:nowrap}
  .contact-phone{position:absolute;font-weight:700;line-height:1;white-space:nowrap}
  .serif{font-family:"Noto Serif",serif}
  .t{position:absolute;line-height:1.1;white-space:nowrap}
  .yellow{color:var(--yellow)}
  .dark{color:var(--ink)}
</style>
</head>
<body>

<!-- 728x90 -->
<div class="size-label" style="left:483px;top:75px">Size : 728x90</div>
<div class="banner leaderboard" style="left:138px;top:132px;width:923px;height:114px">
  <div class="photo photo-dusk" role="img" aria-label="Photo of a two-storey house at dusk" style="left:620px;top:0;width:303px;height:114px;-webkit-mask:linear-gradient(90deg,transparent,#000 30%);mask:linear-gradient(90deg,transparent,#000 30%)"></div>
  <svg class="shapes" viewBox="0 0 923 114" preserveAspectRatio="none">
    <polygon points="0,0 110,0 110,66 152,114 0,114" fill="var(--orange)"/>
    <polygon points="802,0 923,0 923,79" fill="var(--orange)"/>
  </svg>
  <div class="photo photo-day" role="img" aria-label="Photo of a grey suburban house" style="left:24px;top:2px;width:104px;height:61px"></div>
  <svg class="shapes" viewBox="0 0 923 114" preserveAspectRatio="none">
    <rect x="110" y="27" width="190" height="60" rx="7" fill="var(--green)"/>
  </svg>
  <div class="t" style="left:128px;top:31px;width:150px;text-align:right;font-size:9.5px;font-weight:600;line-height:14px;color:var(--white)">WE PAY CASH FOR HOUSES<br>IN <span class="dark">ANY CONDITION !</span></div>
  <div class="t serif dark" style="left:140px;top:63px;width:156px;text-align:center;font-size:6.5px;line-height:9px">Probate, Foreclosure,<br>Pass Due Property Taxes, and more!</div>
  <div class="contact-label" style="left:16px;top:77px;font-size:9.5px">Contact Us:</div>
  <div class="contact-phone dark" style="left:16px;top:91px;font-size:14px">470-555-0193</div>
  <div class="brand" style="left:318px;top:18px;font-size:56px;letter-spacing:5px">ZENTORA</div>
  <div class="read-more" style="left:433px;top:88px;width:56px;height:13px;font-size:7px;line-height:13px">Read More</div>
</div>

<!-- 320x50 -->
<div class="size-label" style="left:748px;top:308px">Size : 320x50</div>
<div class="banner mobile-banner" style="left:138px;top:279px;width:582px;height:91px">
  <div class="photo photo-dusk" role="img" aria-label="Photo of a two-storey house at dusk" style="left:410px;top:0;width:172px;height:91px;-webkit-mask:linear-gradient(90deg,transparent,#000 35%);mask:linear-gradient(90deg,transparent,#000 35%)"></div>
  <svg class="shapes" viewBox="0 0 582 91" preserveAspectRatio="none">
    <polygon points="0,0 20,0 96,91 0,91" fill="var(--orange)"/>
    <polygon points="520,0 582,0 582,42" fill="var(--orange)"/>
  </svg>
  <div class="t" style="left:0;width:480px;top:8px;text-align:center;font-size:12px;font-weight:600">WE PAY CASH FOR HOUSES IN ANY CONDITION !</div>
  <div class="t serif" style="left:0;width:480px;top:24px;text-align:center;font-size:10px;color:#e5f03a">Probate, Foreclosure, Pass Due Property Taxes, and more!</div>
  <div class="brand" style="left:120px;top:52px;font-size:30px">ZENTORA</div>
  <div class="contact-label dark" style="left:16px;top:69px;font-size:5.5px">Contact Us:</div>
  <div class="contact-phone dark" style="left:16px;top:77px;font-size:9px">470-555-0193</div>
  <div class="read-more" style="left:380px;top:70px;width:40px;height:11px;font-size:5.5px;line-height:11px">Read More</div>
</div>

<!-- 160x600 -->
<div class="size-label" style="left:99px;top:727px;transform:translate(-50%,-50%) rotate(-90deg)">Size : 160x600</div>
<div class="banner skyscraper" style="left:138px;top:390px;width:179px;height:671px">
  <svg class="shapes" viewBox="0 0 179 671" preserveAspectRatio="none">
    <polygon points="179,215 179,245 60,262" fill="var(--orange)"/>
    <polygon points="0,420 179,420 179,422 0,463" fill="var(--orange)"/>
    <polygon points="0,470 179,470 179,604 0,604" fill="var(--green)"/>
    <polygon points="0,470 179,470 0,502" fill="#5fb86a" opacity=".45"/>
    <polygon points="0,570 179,590 0,604" fill="#5fb86a" opacity=".45"/>
    <rect x="0" y="623" width="179" height="48" fill="var(--orange)"/>
  </svg>
  <div class="photo photo-dusk" role="img" aria-label="Photo of a two-storey house at dusk" style="left:0;top:243px;width:179px;height:181px;clip-path:polygon(0 12%,100% 0,100% 100%,0 100%)"></div>
  <div class="brand" style="left:0;width:179px;text-align:center;top:30px;font-size:21px">ZENTORA</div>
  <div class="t" style="left:0;width:179px;text-align:center;top:102px;font-size:13px;font-weight:300">WE PAY CASH</div>
  <div class="t yellow" style="left:0;width:179px;text-align:center;top:119px;font-size:22px;font-weight:700">FOR HOUSES</div>
  <div class="t yellow" style="left:0;width:179px;text-align:center;top:144px;font-size:16px;font-weight:700">IN</div>
  <div class="t" style="left:0;width:179px;text-align:center;top:165px;font-size:17px;font-weight:700">ANY CONDITION !</div>
  <div class="read-more" style="left:105px;top:401px;width:61px;height:16px;font-size:8.5px;line-height:16px">Read More</div>
  <div class="t serif" style="left:0;width:179px;text-align:center;top:502px;font-size:13px;line-height:18.5px;color:#f6f6e4">Probate,<br>Foreclosure,<br>Pass Due Property Taxes,<br>and more!</div>
  <div class="contact-label" style="left:0;width:179px;text-align:center;top:626px;font-size:11px">Contact Us:</div>
  <div class="contact-phone dark" style="left:0;width:179px;text-align:center;top:642px;font-size:18px">470-555-0193</div>
</div>

<!-- 300x600 -->
<div class="size-label" style="left:419px;top:1088px">Size : 300x600</div>
<div class="banner half-page" style="left:385px;top:390px;width:335px;height:671px;background:var(--orange)">
  <svg class="shapes" viewBox="0 0 335 671" preserveAspectRatio="none">
    <polygon points="0,46 335,163 335,671 0,671" fill="var(--blue)"/>
    <polygon points="125,26 335,26 335,66 152,66" fill="var(--blue)"/>
    <polygon points="0,336 335,417 335,447 0,340" fill="var(--green)"/>
    <rect x="0" y="586" width="335" height="56" fill="var(--green)"/>
  </svg>
  <div class="photo photo-day" role="img" aria-label="Photo of a beige two-storey house with a porch and garage" style="left:0;top:72px;width:335px;height:345px;clip-path:polygon(0 11%,26% 0,100% 26%,100% 100%,0 76.5%)"></div>
  <div class="contact-label" style="left:0;width:300px;text-align:right;top:30px;font-size:11.5px">Contact Us:</div>
  <div class="contact-phone dark" style="left:0;width:300px;text-align:right;top:44px;font-size:19px">470-555-0193</div>
  <div class="read-more" style="left:230px;top:344px;width:82px;height:24px;font-size:11px;line-height:24px;border-radius:5px">Read More</div>
  <div class="brand" style="left:40px;top:400px;font-size:42px;transform:rotate(14deg);transform-origin:left center">ZENTORA</div>
  <div class="t" style="left:45px;top:480px;font-size:18px;font-weight:300">WE PAY CASH</div>
  <div class="t yellow" style="left:43px;top:509px;font-size:32px;font-weight:700">FOR HOUSES IN</div>
  <div class="t" style="left:45px;top:544px;font-size:24px;font-weight:700">ANY CONDITION !</div>
  <div class="t serif" style="left:0;width:335px;text-align:center;top:594px;font-size:15.5px;line-height:19px;color:#f6f6e4">Probate, Foreclosure,<br>Pass Due Property Taxes, and more!</div>
</div>

<!-- 100x50 -->
<div class="size-label" style="left:789px;top:861px">Size : 100x50</div>
<div class="banner small-square" style="left:753px;top:907px;width:308px;height:154px">
  <div class="photo photo-dusk" role="img" aria-label="Photo of a two-storey house at dusk" style="left:150px;top:22px;width:158px;height:102px;-webkit-mask:linear-gradient(90deg,transparent,#000 30%);mask:linear-gradient(90deg,transparent,#000 30%)"></div>
  <svg class="shapes" viewBox="0 0 308 154" preserveAspectRatio="none">
    <polygon points="0,0 6,0 72,154 0,154" fill="var(--orange)"/>
    <rect x="0" y="122" width="308" height="18" fill="var(--green)"/>
  </svg>
  <div class="brand" style="left:22px;top:13px;font-size:22px">ZENTORA</div>
  <div class="contact-label dark" style="left:0;width:295px;text-align:right;top:19px;font-size:5.5px">Contact Us:</div>
  <div class="contact-phone dark" style="left:0;width:295px;text-align:right;top:27px;font-size:8px">470-555-0193</div>
  <div class="t" style="left:45px;top:55px;font-size:8px;font-weight:300">WE PAY CASH</div>
  <div class="t yellow" style="left:45px;top:67px;font-size:14px;font-weight:700">FOR HOUSES IN</div>
  <div class="t" style="left:46px;top:83px;font-size:9.5px;font-weight:700">ANY CONDITION !</div>
  <div class="t serif dark" style="left:0;width:308px;text-align:center;top:125px;font-size:10.5px">Probate, Foreclosure, Pass Due Property Taxes, and more!</div>
</div>

</body>
</html>
```